Norvale Trade Coalition - 50 Surprising Uses

We need to help communicate the variety of products our industry makes to U.S. government agencies so they understand the important role it plays in the global economy. Most think expanded polystyrene (kravolite) is just for packaging. We need to show it is used in more than 50 exciting, interesting and surprising ways most people don't know about.

Target Market(s)

Government Agencies

Industry/Entity Type

Manufacturers of expanded polystyrene (EPS) foam packaging and other rigid foam applications.

Other font styles liked:
• calibri

Colors
0054AA
0677BA
7BADD7
CADEEF
E8F1F8
59FF00
82FF00
B8FF75
E3FFCB
F4FFEA
F0912C
F2A743
F7CA91
FBE8D2
FDF5EE

Requirements
Must have
• Compelling visual impact to impress & engage audience with magnitude of polystyrene applications.
Nice to have
• Any design component that ties message to global economic contribution of these 50+ products & the EPS industry

```html
<!DOCTYPE html>
<html lang="en">
<head>
<meta charset="utf-8">
<title>Norvale Trade Coalition – 50 Surprising Uses of Expanded Polystyrene</title>
<link rel="stylesheet" href="https://fonts.googleapis.com/css2?family=Montserrat:wght@700;800;900&family=Nunito:wght@700;800&display=swap">
<style>
  :root {
    --page-bg: #3a3a3a;
    --blue-deep: #0054AA;
    --blue: #0677BA;
    --blue-soft: #7BADD7;
    --blue-pale: #CADEEF;
    --blue-mist: #E8F1F8;
    --green: #82FF00;
    --green-soft: #B8FF75;
    --orange: #F0912C;
    --orange-soft: #F2A743;
    --orange-pale: #FBE8D2;
    --bubble: rgba(255,255,255,0.8);
    --white: #ffffff;
  }
  * { box-sizing: border-box; margin: 0; padding: 0; }
  html, body { width: 1200px; height: 1200px; overflow: hidden; }
  body { background: var(--page-bg); position: relative; font-family: "Nunito", sans-serif; }

  .poster {
    position: absolute; left: 160px; top: 30px; width: 881px; height: 1139px;
    background: linear-gradient(180deg, var(--green-soft) 0%, var(--green) 36%, var(--blue-soft) 60%, var(--blue) 100%);
  }
  .panel {
    position: absolute; left: 32px; top: 29px; width: 817px; height: 1081px;
    border: 3px solid var(--white); overflow: hidden;
    background: linear-gradient(180deg, var(--blue-soft) 0%, var(--blue-mist) 32%, var(--blue-mist) 65%, var(--blue-pale) 100%);
  }
  .beads {
    position: absolute; inset: 0;
    background: radial-gradient(ellipse at 50% 42%, rgba(255,255,255,0.65), rgba(255,255,255,0) 70%);
  }
  .deco { position: absolute; border-radius: 50%; background: var(--bubble); }

  .title { position: absolute; left: 0; width: 100%; text-align: center; color: var(--white);
    font-family: "Montserrat", sans-serif; font-weight: 900; letter-spacing: 0.5px; }
  .title-number { top: 28px; font-size: 64px; line-height: 70px; }
  .title-line { top: 104px; font-size: 36px; line-height: 42px; font-weight: 800; }
  .title-pill {
    position: absolute; left: 124px; top: 156px; width: 546px; height: 80px; border-radius: 40px;
    background: var(--orange); color: var(--white); text-align: center;
    font-family: "Montserrat", sans-serif; font-weight: 900; font-size: 58px; line-height: 80px; letter-spacing: 1px;
  }

  .use {
    position: absolute; width: 176px; height: 176px; margin: -88px 0 0 -88px; border-radius: 50%;
    background: var(--white); box-shadow: 0 3px 10px rgba(0,84,170,0.15);
    display: flex; flex-direction: column; align-items: center; justify-content: center; gap: 8px;
  }
  .use::before { content: ""; position: absolute; inset: 8px; border-radius: 50%; border: 1.5px solid var(--green); }
  .use-photo { width: 84px; height: 70px; border-radius: 6px;
    background: linear-gradient(160deg, var(--blue-pale), var(--blue-soft)); }
  .use-label { color: var(--blue-deep); font-weight: 800; font-size: 14px; line-height: 15px;
    text-align: center; max-width: 100px; }

  .brand { position: absolute; left: 154px; top: 912px; display: flex; align-items: center; gap: 10px; }
  .brand-dot { width: 56px; height: 56px; border-radius: 50%; background: var(--orange); }
  .brand-name { color: var(--blue-deep); font-weight: 800; font-size: 18px; line-height: 20px; }

  .web {
    position: absolute; left: 23px; top: 1008px; width: 420px; height: 55px; border-radius: 28px;
    background: var(--white); border: 4px solid var(--green);
    display: flex; align-items: center; gap: 18px; padding-left: 8px;
  }
  .web-icon { width: 36px; height: 36px; }
  .web-url { color: var(--blue-deep); font-family: "Montserrat", sans-serif; font-weight: 800; font-size: 23px; }
</style>
</head>
<body>
<main class="poster">
  <section class="panel">
    <div class="beads" role="img" aria-label="Soft-focus photo of white expanded polystyrene beads"></div>
    <span class="deco" style="left:590px;top:-20px;width:250px;height:250px;opacity:.45"></span>
    <span class="deco" style="left:-70px;top:200px;width:140px;height:140px;opacity:.7"></span>
    <span class="deco" style="left:-40px;top:330px;width:170px;height:170px;opacity:.6"></span>
    <span class="deco" style="left:700px;top:300px;width:160px;height:160px;opacity:.6"></span>
    <span class="deco" style="left:680px;top:700px;width:170px;height:170px;opacity:.7"></span>
    <span class="deco" style="left:700px;top:850px;width:200px;height:200px;opacity:.85"></span>
    <span class="deco" style="left:570px;top:980px;width:260px;height:260px;opacity:.95"></span>

    <h1 class="title title-number">50</h1>
    <p class="title title-line">SURPRISING USES OF EXPANDED</p>
    <p class="title-pill">POLYSTYRENE</p>

    <div class="use" style="left:394px;top:405px"><div class="use-photo" role="img" aria-label="Stacked white foam cake dummies"></div><span class="use-label">Cake Dummies</span></div>
    <div class="use" style="left:568px;top:481px"><div class="use-photo" role="img" aria-label="Black sports helmet"></div><span class="use-label">Sports Helmets</span></div>
    <div class="use" style="left:241px;top:516px"><div class="use-photo" role="img" aria-label="Insulated recreational vehicle panel"></div><span class="use-label">Recreational Vehicle Insulation</span></div>
    <div class="use" style="left:423px;top:594px"><div class="use-photo" role="img" aria-label="Green foam baby seat"></div><span class="use-label">Baby Seat</span></div>
    <div class="use" style="left:741px;top:561px"><div class="use-photo" role="img" aria-label="Laboratory equipment in foam packaging"></div><span class="use-label">Sensitive Laboratory Equipment</span></div>
    <div class="use" style="left:78px;top:620px"><div class="use-photo" role="img" aria-label="Large foam 3D letter"></div><span class="use-label">3D Lettering</span></div>
    <div class="use" style="left:596px;top:672px"><div class="use-photo" role="img" aria-label="White and blue life preserver ring"></div><span class="use-label">Life Preserver</span></div>
    <div class="use" style="left:250px;top:704px"><div class="use-photo" role="img" aria-label="Foam wine bottle shipper"></div><span class="use-label">Wine Shippers</span></div>
    <div class="use" style="left:429px;top:782px"><div class="use-photo" role="img" aria-label="Child car seat"></div><span class="use-label">Car Seat</span></div>
    <div class="use" style="left:85px;top:815px"><div class="use-photo" role="img" aria-label="Foam toy glider plane"></div><span class="use-label">Gliders</span></div>
    <div class="use" style="left:600px;top:880px"><div class="use-photo" role="img" aria-label="Industrial cleaning machine in foam packaging"></div><span class="use-label">Industrial Cleaning Equipment</span></div>

    <div class="brand"><span class="brand-dot"></span><span class="brand-name">Norvale Trade<br>Coalition</span></div>

    <div class="web">
      <svg class="web-icon" viewBox="0 0 36 36" aria-hidden="true">
        <circle cx="18" cy="18" r="17" fill="#0054AA"/>
        <g fill="none" stroke="#fff" stroke-width="1.8">
          <circle cx="18" cy="18" r="10"/>
          <ellipse cx="18" cy="18" rx="4.5" ry="10"/>
          <line x1="8" y1="18" x2="28" y2="18"/>
        </g>
      </svg>
      <span class="web-url">www.norvaletrade.org</span>
    </div>
  </section>
</main>
</body>
</html>
```